Mental Health & Addiction Podcast Art

Project: Podcast Cover Art / Visual Identity
Podcast Name: The Renewal Compass
Focus: Recovery from substance use and mental health
Objectives
Create compelling podcast artwork that:
Reflects the themes of hope, healing, and personal growth
Establishes credibility and professionalism
Appeals to individuals seeking recovery resources and support
Maintains strong brand consistency with Harborline Wellness
Brand Integration Requirements
Logo incorporation: Integrate an element from the Harborline Wellness Logo—potentially an abstract or partial use of the sun motif
Flexibility: Open to creative interpretations (e.g., sun rays as background texture, sunrise gradient, partial sun as a design accent)
Mandatory: Must adhere to existing Harborline Wellness brand guidelines (approved color palette, typography, and visual style)

Target Market(s)

United states, people with addiction and mental health disorders.

Industry/Entity Type

Wellness

Font styles to use
Other font styles liked:
• See Brand Guide

Requirements
Must have
• Match brand guide, in corporate elements of the Harborline Wellness Logo icon

```html
<!DOCTYPE html>
<html lang="en">
<head>
<meta charset="utf-8">
<title>The Renewal Compass — Podcast Cover</title>
<link href="https://fonts.googleapis.com/css2?family=Montserrat:wght@500;800;900&display=swap" rel="stylesheet">
<style>
  :root {
    --page: #ffffff;
    --navy: #152e45;
    --sun: #f0b042;
    --white: #ffffff;
    --skin-light: #e9dccb;
    --skin-mid: #b07a55;
    --hair: #1d1a1a;
  }
  html, body {
    margin: 0;
    padding: 0;
    width: 1200px;
    height: 1083px;
    overflow: hidden;
    background: var(--page);
  }
  .cover {
    position: absolute;
    left: 213px;
    top: 155px;
    width: 774px;
    height: 774px;
    box-shadow: 0 6px 18px rgba(0, 0, 0, 0.18);
    overflow: hidden;
  }
  .cover svg {
    display: block;
  }
  .brand-name {
    font-family: "Montserrat", sans-serif;
    font-weight: 500;
    font-size: 26px;
    fill: var(--white);
  }
  .title {
    font-family: "Montserrat", sans-serif;
    font-weight: 900;
    fill: var(--white);
  }
  .title-small { font-size: 52px; }
  .title-mid { font-size: 66px; }
  .title-big { font-size: 118px; }
  .sun-ray {
    stroke: var(--sun);
    stroke-linecap: round;
    fill: none;
  }
</style>
</head>
<body>
  <div class="cover">
    <svg width="774" height="774" viewBox="0 0 774 774" xmlns="http://www.w3.org/2000/svg">
      <defs>
        <linearGradient id="portraitTone" x1="0" y1="0" x2="0" y2="1">
          <stop offset="0" stop-color="var(--hair)"/>
          <stop offset="0.35" stop-color="var(--skin-mid)"/>
          <stop offset="0.7" stop-color="var(--skin-light)"/>
          <stop offset="1" stop-color="#cdb498"/>
        </linearGradient>
      </defs>

      <rect class="backdrop" x="0" y="0" width="774" height="774" fill="var(--navy)"/>

      <g class="sun-rays">
        <line class="sun-ray" x1="638" y1="52" x2="638" y2="150" stroke-width="33"/>
        <line class="sun-ray" x1="428" y1="114" x2="545" y2="318" stroke-width="34"/>
        <line class="sun-ray" x1="272" y1="272" x2="545" y2="410" stroke-width="38"/>
        <line class="sun-ray" x1="230" y1="479" x2="440" y2="476" stroke-width="42"/>
      </g>

      <path class="host-portrait" role="img" aria-label="Portrait photo of the podcast host smiling and looking to the side"
            d="M510 230 Q540 90 640 78 Q740 80 774 140 L774 665 L300 665 Q360 560 395 500 Q440 410 520 370 Q495 300 510 230 Z"
            fill="url(#portraitTone)"/>

      <g class="brand-lockup">
        <circle cx="224" cy="84" r="30" fill="none" stroke="var(--white)" stroke-width="2.5"/>
        <text class="brand-name" x="58" y="156" textLength="332" lengthAdjust="spacingAndGlyphs">HARBORLINE WELLNESS</text>
      </g>

      <rect class="base-band" x="0" y="665" width="774" height="109" fill="var(--sun)"/>

      <g class="podcast-title">
        <text class="title title-small" x="71" y="502" textLength="93" lengthAdjust="spacingAndGlyphs">THE</text>
        <text class="title title-mid" x="71" y="566" textLength="340" lengthAdjust="spacingAndGlyphs">RENEWAL</text>
        <text class="title title-big" x="70" y="696" textLength="530" lengthAdjust="spacingAndGlyphs">COMPASS</text>
      </g>
    </svg>
  </div>
</body>
</html>
```